International Student Travel Company needs a web page re-designed

Halvard Tours is a worldwide leader in student educational and performing arts travel programs. We provide high-quality tours that exceed the expectations of our participants/customers and enhance a student's learning experiences. Our mission is to forever change how every student sees the world around them. Our company has 3 distinct brands: Halvard Tours (www.halvardtours.example), Meridale Tours (www.meridaletours.example) and Pellwood Legacy Tours & Music Galas (www.pellgala.example).

As part of our travel programs, we offer participants the option to purchase travel insurance. We are looking to re-design the page that offers each participant the option to buy insurance during their online registration process to maximize the number of customers who purchase the recommended option. The registration process is set up behind a password protected registration website.

Here is a link to view the current page for each brand:
https://accounts.halvardtours.example/tech/demo/8656
https://accounts.meridaletours.example/tech/demo/8656
https://accounts.pellgala.example/tech/demo/8656

We are attaching the HTML for the current page so you can start with the current format that this design is a part of- for example, the header & footer and the "Registration Step # section".

Please note that this current design was created for the "Meridale Tours" brand as you may note the use of the orange color on the page. We would like to design the page so that we can easily implement the same design for all 3 brands. As you will see from looking at the brands online, they all share a similar blue that can be used where we need a color as you will see on our SAMPLE mock-up that we have included as an attachment.

In our SAMPLE mock-up (file attached named "SAMPLE webpage mock-up.pdf") we have icons at the top of the insurance option which is meant to be a link to a PDF that is an advertisement for each type of travel insurance. So, however you decide to design that element, please make sure to include that as a link that will open a PDF in a new tab. The "None" option will open up the PDF attached named "Note to Parents.pdf". The "Scholar Prime" option will open up the PDF attached named "Odette & Marla.pdf". The "Scholar Prime with CFAR" option will open up the PDF attached named "CFAR.pdf".

The sample mock-up is just a sample draft idea of how we would want it to look. Please feel free to re-design completely or as close to this design as you wish using your best design judgment. The goal is to make it look very professional and convince customers to select the recommended "Scholar Prime with CFAR" option as this will fully protect them in case they need to cancel.

It is very important to use all the copy as its presented since the language has all been approved by the insurance company's compliance team.

*VERY IMPORTANT*
Please design this so that it is MOBILE friendly. Many of our customers register for our trips on their mobile devices. So, because we are presenting 3 options to compare we need to make sure the design works well on small mobile screens. So, please present your designs for both large computer screens and small mobile devices so we can see how it would look at the various different screen sizes.

Please let us know if you have any questions or require any more info from us to get started. We are looking forward to seeing your designs!

-Halvard Tours Marketing Team

```html
<!DOCTYPE html>
<html lang="en">
<head>
<meta charset="utf-8">
<title>Halvard Tours – Registration Step 5/8 – Travel Protection</title>
<link href="https://fonts.googleapis.com/css2?family=Roboto:wght@400;500;700;900&display=swap" rel="stylesheet">
<style>
:root{
  --blue-deep:#0b3a9c;
  --blue-bright:#1a5fd8;
  --blue-footer:#0b6cb5;
  --red:#d6282f;
  --yellow:#ffba00;
  --ink:#222;
  --muted:#666;
  --rule:#e4e4e4;
  --panel:#f3f4fa;
  --white:#fff;
}
*{box-sizing:border-box;margin:0;padding:0}
html,body{width:728px;height:1200px;overflow:hidden;background:var(--white)}
body{font-family:"Roboto",Arial,sans-serif;color:var(--ink)}
a{color:inherit;text-decoration:none}
.stage{position:absolute;left:0;top:0;width:1512px;height:2490px;transform:scale(.4815);transform-origin:0 0}
.abs{position:absolute}

.view-title{position:absolute;font-weight:700;color:#000;line-height:1}

/* shared bits */
.brand{display:flex;align-items:center;gap:6px;color:var(--blue-deep);font-weight:500}
.brand-dot{background:var(--red);border-radius:50%;flex:none}
.tour-info{border:1px solid var(--rule);background:#fff}
.tour-info h4{font-weight:400;color:#333;border-bottom:1px solid var(--rule);background:#f6f6f6}
.tour-info p{color:var(--muted)}
.tour-info b{color:#333}
.reg-head{display:flex;justify-content:space-between;align-items:baseline;color:#222;white-space:nowrap}
.reg-head .step-num{color:var(--red);font-weight:700}
.photo{background:linear-gradient(180deg,#7fb0e6 0%,#b9d3ee 38%,#8a9a6a 62%,#4f6b34 100%)}
.hero-band{position:absolute;background:var(--blue-deep);color:#fff;display:flex;align-items:center}
.partner{display:flex;align-items:center;gap:4px;font-weight:700;color:#fff;flex:none}
.partner-mark{background:#fff;flex:none}
.protect-title{color:var(--blue-deep);font-weight:900}
.lede{color:#222}
.trip-cost{color:var(--red);font-weight:500}

.plan{position:absolute;background:var(--blue-deep);color:#fff;text-align:center}
.plan-pdf{position:absolute;border-radius:50%;background:var(--blue-bright);border:2px solid #fff;display:flex;align-items:center;justify-content:center;z-index:2}
.plan-tag{position:absolute;background:var(--red);color:#fff;text-align:center}
.plan-name{font-weight:700}
.plan-price{font-weight:700}
.plan-price sup{font-size:.55em;font-weight:400}
.plan-pitch{font-weight:700}
.plan-list{list-style:none;text-align:left}
.plan-list li{position:relative}
.plan-list li.is-yes::before{content:"";position:absolute;left:1px;top:.2em;width:.6em;height:.32em;border-left:1.2px solid #fff;border-bottom:1.2px solid #fff;transform:rotate(-45deg)}
.plan-list li.is-no{color:var(--red)}
.plan-list li.is-no::before{content:"✕";position:absolute;left:0;top:0}
.plan-list li.is-dot::before{content:"";position:absolute;left:.3em;top:.45em;width:3px;height:3px;border-radius:50%;background:#fff}
.plan-select{position:absolute;left:50%;transform:translateX(-50%);background:var(--blue-bright);color:#fff;font-weight:700;border-radius:20px;text-align:center}

.benefits{border-collapse:collapse;position:absolute;table-layout:fixed}
.benefits th{font-weight:700;text-align:left;vertical-align:bottom}
.benefits td{border-top:1px solid var(--rule);vertical-align:middle}
.benefits tr:nth-child(even) td{background:var(--panel)}
.benefits .b-name{font-weight:700}
.x{color:var(--red);font-weight:300}
.tick{display:inline-block;width:11px;height:6px;border-left:2px solid var(--blue-bright);border-bottom:2px solid var(--blue-bright);transform:rotate(-45deg)}
.notes{color:#444}
.notes p+p{margin-top:1em}
.limits-btn{position:absolute;background:var(--blue-bright);color:#fff;border-radius:14px;text-align:center}
.site-foot{position:absolute;background:var(--blue-footer);color:#fff;font-weight:700}
.seal{background:#fff;border:2px solid #6cae3a;border-radius:2px;display:inline-block}

/* desktop */
.d-title{left:271px;top:62px;font-size:32px}
.d-covid{left:0;top:110px;width:946px;height:32px;background:var(--yellow);font-size:9px;font-weight:500;display:flex;align-items:center;justify-content:center}
.d-header{left:0;top:142px;width:946px;height:49px;border-bottom:1px solid var(--rule)}
.d-header .brand{position:absolute;left:177px;top:8px;font-size:16px}
.d-header .brand-dot{width:32px;height:32px}
.d-signed{position:absolute;left:597px;top:18px;font-size:7.5px;color:var(--muted)}
.d-signed a{color:var(--red);margin-left:5px}
.d-tab{left:0;top:338px;width:15px;height:112px;background:var(--blue-bright);color:#fff;font-size:6.5px;writing-mode:vertical-rl;transform:rotate(180deg);display:flex;align-items:center;justify-content:center;border-radius:0 3px 3px 0}
.d-reg{left:583px;top:212px;width:187px}
.d-reg .reg-head{font-size:16px;margin-bottom:6px}
.d-reg .tour-info h4{font-size:7.5px;padding:6px 8px}
.d-reg .tour-info p{font-size:7px;padding:0 8px;line-height:15.5px;white-space:nowrap}
.d-reg .tour-info div{padding:14px 0 8px}
.d-hero{left:173px;top:215px;width:396px;height:263px}
.d-hero .hero-band{left:8px;top:208px;width:381px;height:55px;padding:0 8px 0 12px;gap:12px}
.d-hero .partner{font-size:7px;width:100px}
.d-hero .partner-mark{width:16px;height:16px}
.d-hero .hero-copy{font-size:8.2px;font-weight:700;line-height:11.2px;text-transform:uppercase}
.d-content{left:181px;top:494px;width:380px}
.d-content .protect-title{font-size:16px;line-height:22px}
.d-content .lede{font-size:7.8px;line-height:12.4px;margin-top:10px}
.d-content .lede+.lede{margin-top:12px}
.d-content .trip-cost{font-size:12px;margin:16px 0 0 6px}
.d-plans{left:173px;top:660px;width:396px;height:318px;background:var(--panel)}
.d-plans .band{position:absolute;left:0;top:237px;width:396px;height:81px;background:var(--blue-bright)}
.d-plans .plan{top:16px;width:123px;height:270px;padding:16px 7px 0}
.d-plans .plan-pdf{width:24px;height:24px;top:-16px;left:-4px}
.d-plans .plan-tag{left:266px;top:0;width:123px;height:16px;font-size:8px;line-height:16px;z-index:1}
.d-plans .plan-name{font-size:9px;line-height:12px}
.d-plans .plan-price{font-size:12px;margin:4px 0 16px}
.d-plans .plan-pitch{font-size:7px;line-height:10px;margin-bottom:12px}
.d-plans .plan-list{font-size:6.4px;line-height:10px}
.d-plans .plan-list li{padding-left:10px;margin-bottom:9px}
.d-plans .plan-select{bottom:-14px;width:78px;height:22px;font-size:8.5px;line-height:22px}
.d-table{left:173px;top:990px;width:396px}
.d-table th{font-size:7.5px;height:30px;padding:0 2px 5px;line-height:9px}
.d-table th.b-head{font-size:12px;font-weight:500;padding-left:8px}
.d-table td{font-size:6.6px;padding:0 2px}
.d-table .b-name{font-size:6.5px;line-height:10px}
.d-notes{left:173px;top:1352px;width:396px;font-size:6.2px;line-height:10px}
.d-limits{left:174px;top:1500px;width:189px;height:22px;font-size:8.5px;line-height:22px}
.d-foot{left:0;top:1585px;width:946px;height:33px;font-size:7.5px;display:flex;align-items:center;justify-content:center;gap:8px}
.d-foot .seal{width:70px;height:18px;margin-left:24px}

/* mobile */
.m-title{left:1177px;top:70px;font-size:30px}
.m{left:1172px;width:185px}
.m-header{top:116px;height:42px;border-bottom:1px solid var(--rule)}
.m-header .brand{position:absolute;left:7px;top:5px;font-size:12px}
.m-header .brand-dot{width:26px;height:26px}
.m-menu{position:absolute;right:8px;top:8px;width:22px;height:20px;background:var(--blue-deep);display:flex;flex-direction:column;justify-content:center;gap:3px;padding:0 5px}
.m-menu i{display:block;height:1.5px;background:#fff}
.m-reg{top:174px;padding:0 7px}
.m-reg .reg-head{font-size:12px;margin-bottom:4px}
.m-reg .tour-info h4{font-size:5px;padding:4px 6px}
.m-reg .tour-info div{padding:6px 0 4px}
.m-reg .tour-info p{font-size:4.6px;padding:0 6px;line-height:12.5px;white-space:nowrap}
.m-hero{top:278px;height:149px}
.m-hero .hero-band{left:0;top:97px;width:185px;height:52px;padding:0 4px;gap:4px}
.m-hero .partner{font-size:3.6px;width:46px}
.m-hero .partner-mark{width:7px;height:7px}
.m-hero .hero-copy{font-size:5.3px;line-height:8.8px}
.m-content{top:427px;height:258px;background:var(--panel);padding:12px 8px 0}
.m-content .protect-title{font-size:12px;line-height:15px}
.m-content .lede{font-size:7.2px;line-height:12.3px;margin-top:10px}
.m-content .lede+.lede{margin-top:12px}
.m-content .trip-cost{font-size:10px;line-height:13px;margin-top:8px}
.m-plans{top:685px;height:720px;background:var(--panel)}
.m-plans .plan{left:10px;width:166px;padding:16px 8px 0}
.m-plans .plan-pdf{width:22px;height:22px;top:-12px;left:-9px}
.m-plans .plan-tag{left:10px;top:2px;width:166px;height:18px;font-size:7.5px;line-height:18px}
.m-plans .plan-name{font-size:11.5px;line-height:15px}
.m-plans .plan-price{font-size:10.5px;margin:6px 0 12px}
.m-plans .plan-pitch{font-size:6.4px;line-height:9.5px;margin-bottom:8px}
.m-plans .plan-list{font-size:6px;line-height:10px}
.m-plans .plan-list li{padding-left:12px;margin-bottom:6px}
.m-plans .plan-select{bottom:-12px;width:82px;height:22px;font-size:8.5px;line-height:22px}
.m-table{left:1172px;top:1412px;width:185px}
.m-table th{font-size:6.5px;height:28px;padding:0 2px 4px;line-height:9px}
.m-table th.b-head{font-size:12px;font-weight:500;padding-left:5px}
.m-table td{font-size:6.5px;padding:0 2px}
.m-table .b-name{font-size:5.4px;line-height:10px;padding-left:5px}
.m-scroll{left:1220px;top:1751px;width:100px;height:3px;background:#333;border-radius:2px}
.m-notes{left:1172px;top:1768px;width:185px;padding:0 9px;font-size:6.3px;line-height:10px}
.m-limits{left:1192px;top:2020px;width:146px;height:16px;font-size:6px;line-height:16px}
.m-foot{left:1172px;top:2048px;width:185px;height:35px;font-size:3.6px;padding:4px 6px;text-align:center;line-height:7px}
.m-foot .seal{position:absolute;left:4px;top:17px;width:42px;height:13px}
</style>
</head>
<body>
<div class="stage">

  <!-- ===== Desktop ===== -->
  <h1 class="view-title d-title">Desktop View</h1>

  <div class="abs d-covid"><a href="#">For Coronavirus (COVID-19) Updates Please Click Here</a></div>

  <header class="abs d-header">
    <div class="brand"><span class="brand-dot"></span>Halvard Tours</div>
    <div class="d-signed">signed on as webuser@example.com <a href="#">[Logout]</a></div>
  </header>

  <a class="abs d-tab" href="#">Questions? Comments?</a>

  <section class="abs photo d-hero" role="img" aria-label="Photo of smiling students taking a group selfie in front of the Eiffel Tower">
    <div class="hero-band">
      <div class="partner"><span class="partner-mark"></span>WAYFARER ASSURANCE</div>
      <p class="hero-copy">Travel insurance is optional, but unexpected events are always a possibility… and without the Scholar Prime Group Travel Protection, you might lose up to 100% of your trip investment</p>
    </div>
  </section>

  <aside class="abs d-reg">
    <div class="reg-head"><span>Registration</span><span>Step <span class="step-num">5</span>/8</span></div>
    <div class="tour-info">
      <h4>YOUR TOUR INFORMATION</h4>
      <div>
        <p>Group Name: <b>Brookfield Elementary School</b></p>
        <p>Tour Name: <b>Two Days Test Tour</b></p>
        <p>Tour Dates: <b>3/2/2021</b></p>
        <p>Tour Organizer: <b>Mr. Corwin Testa</b></p>
      </div>
    </div>
  </aside>

  <section class="abs d-content">
    <h2 class="protect-title">PROTECT YOUR TRIP INVESTMENT!</h2>
    <p class="lede">Wayfarer Assurance Group, a leading provider of group travel insurance, offers participants the opportunity to protect their travel investment.</p>
    <p class="lede">This program offers an array of <b>travel protection</b> benefits including 24/7 Worldwide Non-Insurance Assistance Services as well as Trip Cancellation, Trip Interruption, Medical Expense, Baggage and Personal Effects, and more travel insurance coverages such as the Cancel for Any Reason (CFAR) option, if eligible.</p>
    <p class="trip-cost">To start, please enter your total Trip Cost: $_______</p>
  </section>

  <section class="abs d-plans">
    <div class="band"></div>
    <div class="plan-tag">RECOMMENDED</div>

    <article class="plan" style="left:8px">
      <a class="plan-pdf" href="Note to Parents.pdf" target="_blank" aria-label="Open Note to Parents PDF"><svg width="14" height="14" viewBox="0 0 14 14"><rect x="2.5" y="1" width="9" height="12" rx="1" fill="none" stroke="#fff" stroke-width="1.2"/><text x="7" y="9" font-size="4.5" font-family="Roboto,sans-serif" font-weight="700" fill="#fff" text-anchor="middle">PDF</text></svg></a>
      <h3 class="plan-name">NONE</h3>
      <p class="plan-price"><sup>$</sup>0</p>
      <p class="plan-pitch">Potentially lose 100% of your tour cost</p>
      <ul class="plan-list"><li class="is-dot">No Payment Protection</li></ul>
      <a class="plan-select" href="#">SELECT</a>
    </article>

    <article class="plan" style="left:137px">
      <a class="plan-pdf" href="Odette & Marla.pdf" target="_blank" aria-label="Open Scholar Prime PDF"><svg width="14" height="14" viewBox="0 0 14 14"><rect x="2.5" y="1" width="9" height="12" rx="1" fill="none" stroke="#fff" stroke-width="1.2"/><text x="7" y="9" font-size="4.5" font-family="Roboto,sans-serif" font-weight="700" fill="#fff" text-anchor="middle">PDF</text></svg></a>
      <h3 class="plan-name">SCHOLAR PRIME</h3>
      <p class="plan-price"><sup>$</sup>100</p>
      <p class="plan-pitch">Protects your trip investment for covered reasons only</p>
      <ul class="plan-list">
        <li class="is-yes">Trip Cancellation coverage provides a 100% refund if you need to cancel for covered reasons</li>
        <li class="is-yes">Includes additional coverages as per below Schedule</li>
        <li class="is-no">Does NOT include Cancel for Any Reason (CFAR)***</li>
        <li class="is-no">No coverage for cancellations due to fear of a pandemic</li>
      </ul>
      <a class="plan-select" href="#">SELECT</a>
    </article>

    <article class="plan" style="left:266px">
      <a class="plan-pdf" href="CFAR.pdf" target="_blank" aria-label="Open CFAR PDF"><svg width="14" height="14" viewBox="0 0 14 14"><rect x="2.5" y="1" width="9" height="12" rx="1" fill="none" stroke="#fff" stroke-width="1.2"/><text x="7" y="9" font-size="4.5" font-family="Roboto,sans-serif" font-weight="700" fill="#fff" text-anchor="middle">PDF</text></svg></a>
      <h3 class="plan-name">SCHOLAR PRIME<br>WITH CFAR</h3>
      <p class="plan-price" style="margin-bottom:8px"><sup>$</sup>150</p>
      <p class="plan-pitch">Protects your trip investment if you need to cancel for any reason***</p>
      <ul class="plan-list">
        <li class="is-yes">Trip Cancellation coverage provides a 100% refund if you need to cancel for covered reasons</li>
        <li class="is-yes">Includes additional coverages as per below Schedule</li>
        <li class="is-yes">Includes Cancel for Any Reason (CFAR)***</li>
        <li class="is-yes">Covers cancellation due to fear of a pandemic ***</li>
      </ul>
      <a class="plan-select" href="#">SELECT</a>
    </article>
  </section>

  <table class="benefits d-table">
    <colgroup><col style="width:133px"><col style="width:50px"><col style="width:102px"><col></colgroup>
    <tr><th class="b-head">Benefit</th><th>NONE</th><th>SCHOLAR PRIME</th><th>SCHOLAR PRIME<br>WITH CFAR</th></tr>
    <tr style="height:27px"><td class="b-name">CANCEL FOR ANY REASON (CFAR)***</td><td class="x">✕</td><td class="x">✕</td><td><span class="tick"></span></td></tr>
    <tr style="height:25px"><td class="b-name">Trip Cancellation**</td><td class="x">✕</td><td>Trip Cost*</td><td>Trip Cost*</td></tr>
    <tr style="height:24px"><td class="b-name">Trip Interruption**</td><td class="x">✕</td><td>150% Trip Cost</td><td>150% Trip Cost</td></tr>
    <tr style="height:24px"><td class="b-name">Travel Delay – 6 Hours</td><td class="x">✕</td><td>$750 ($150/day)</td><td>$750 ($150/day)</td></tr>
    <tr style="height:32px"><td class="b-name">Missed Connection –<br>3 Hours</td><td class="x">✕</td><td>$500</td><td>$500</td></tr>
    <tr style="height:25px"><td class="b-name">Baggage/Personal Effects</td><td class="x">✕</td><td>$1,500</td><td>$1,500</td></tr>
    <tr style="height:23px"><td class="b-name">Baggage Delay – 24 Hours</td><td class="x">✕</td><td>$300</td><td>$300</td></tr>
    <tr style="height:38px"><td class="b-name">Emergency Medical Evacuation, Medical Repatriation &amp; Return of Remains</td><td class="x">✕</td><td>$100,000</td><td>$100,000</td></tr>
    <tr style="height:32px"><td class="b-name">Accident &amp; Sickness Medical Expense</td><td class="x">✕</td><td>$25,000</td><td>$25,000</td></tr>
    <tr style="height:31px"><td class="b-name">Non-Medical Emergency Evacuation</td><td class="x">✕</td><td>$100,000</td><td>$100,000</td></tr>
    <tr style="height:29px"><td class="b-name">Non-Insurance Worldwide Emergency Assistance Services</td><td class="x">✕</td><td>Included</td><td>Included</td></tr>
  </table>

  <div class="abs notes d-notes">
    <p>Coverages may vary and not all coverage is available in all jurisdictions. Totals listed below each coverage are the maximum benefit amount payable.</p>
    <p>* Up to the lesser of the Trip Cost paid or the limit of Coverage for which benefits are requested and the appropriate plan cost has been paid. Maximum limit of $10,000</p>
    <p>** For $0 Trip Cost, there is no Trip Cancellation and Trip Interruption is limited to $500 return air only</p>
    <p>*** CFAR coverage is the lessor of 75% of the nonrefundable trip cost or up to the maximum of $10,000. CFAR is optional and available for purchase on an individual level. Trip cancellation must be 48 hours or more prior to scheduled departure. CFAR must be purchased at the time of plan purchase and with, or before your final payment. CFAR is available if you paid your Travel Supplier for the full cost for all non-refundable trip costs for your trip prior to your cancellation of your trip. For $0 Trip Cost there is no CFAR. <b>This benefit is not available to residents of New York State.</b></p>
  </div>

  <a class="limits-btn d-limits" href="#">Click here for limitations and exclusions</a>

  <footer class="d-foot site-foot">
    <span>© 2020 HALVARD TOURS, INC. RS, INC.</span><span>CONTACT US</span><span>(800) 555-0142</span><span>PRIVACY POLICY</span><span>RESPONSIBILITY</span><span class="seal"></span>
  </footer>

  <!-- ===== Mobile ===== -->
  <h1 class="view-title m-title">Mobile View</h1>

  <header class="abs m m-header">
    <div class="brand"><span class="brand-dot"></span>Halvard Tours</div>
    <div class="m-menu" aria-label="Menu"><i></i><i></i><i></i></div>
  </header>

  <aside class="abs m m-reg">
    <div class="reg-head"><span>Registration</span><span>Step <span class="step-num">5</span>/8</span></div>
    <div class="tour-info">
      <h4>YOUR TOUR INFORMATION</h4>
      <div>
        <p>Group Name: <b>Brookfield Elementary School</b></p>
        <p>Tour Name: <b>Two Days Test Tour</b></p>
        <p>Tour Dates: <b>3/2/2021</b></p>
        <p>Tour Organizer: <b>Mr. Corwin Testa</b></p>
      </div>
    </div>
  </aside>

  <section class="abs m photo m-hero" role="img" aria-label="Photo of smiling students taking a group selfie in front of the Eiffel Tower">
    <div class="hero-band">
      <div class="partner"><span class="partner-mark"></span>WAYFARER ASSURANCE</div>
      <p class="hero-copy">Travel Insurance is optional, but unexpected events are always a possibility… and without the Scholar Prime Group Travel Protection, you might lose up to 100% of your trip investment.</p>
    </div>
  </section>

  <section class="abs m m-content">
    <h2 class="protect-title">PROTECT YOUR TRIP INVESTMENT!</h2>
    <p class="lede">Wayfarer Assurance Group, a leading provider of group travel insurance, offers participants the opportunity to protect their travel investment.</p>
    <p class="lede">This program offers an array of <b>travel protection</b> benefits including 24/7 Worldwide Non-Insurance Assistance Services as well as Trip Cancellation, Trip Interruption, Medical Expense, Baggage and Personal Effects, and more travel insurance coverages such as the Cancel for Any Reason (CFAR) option, if eligible.</p>
    <p class="trip-cost">To start, please enter your total Trip Cost: $_______</p>
  </section>

  <section class="abs m m-plans">
    <div class="plan-tag">RECOMMENDED</div>

    <article class="plan" style="top:20px;height:230px">
      <a class="plan-pdf" href="CFAR.pdf" target="_blank" aria-label="Open CFAR PDF" style="top:-20px"><svg width="13" height="13" viewBox="0 0 14 14"><rect x="2.5" y="1" width="9" height="12" rx="1" fill="none" stroke="#fff" stroke-width="1.2"/><text x="7" y="9" font-size="4.5" font-family="Roboto,sans-serif" font-weight="700" fill="#fff" text-anchor="middle">PDF</text></svg></a>
      <h3 class="plan-name">SCHOLAR PRIME<br>WITH CFAR</h3>
      <p class="plan-price"><sup>$</sup>150</p>
      <p class="plan-pitch">Protects your trip investment if you need to cancel for any reason***</p>
      <ul class="plan-list">
        <li class="is-yes">Trip Cancellation coverage provides a 100% refund if you need to cancel for covered reasons</li>
        <li class="is-yes">Includes additional coverages as per below Schedule</li>
        <li class="is-yes">Includes Cancel for Any Reason (CFAR)***</li>
        <li class="is-yes">Covers cancellation due to fear of a pandemic ***</li>
      </ul>
      <a class="plan-select" href="#">SELECT</a>
    </article>

    <article class="plan" style="top:288px;height:228px">
      <a class="plan-pdf" href="Odette & Marla.pdf" target="_blank" aria-label="Open Scholar Prime PDF"><svg width="13" height="13" viewBox="0 0 14 14"><rect x="2.5" y="1" width="9" height="12" rx="1" fill="none" stroke="#fff" stroke-width="1.2"/><text x="7" y="9" font-size="4.5" font-family="Roboto,sans-serif" font-weight="700" fill="#fff" text-anchor="middle">PDF</text></svg></a>
      <h3 class="plan-name">SCHOLAR PRIME</h3>
      <p class="plan-price"><sup>$</sup>100</p>
      <p class="plan-pitch">Protects your trip investment for covered reasons only</p>
      <ul class="plan-list">
        <li class="is-yes">Trip Cancellation coverage provides a 100% refund if you need to cancel for covered reasons</li>
        <li class="is-yes">Includes additional coverages as per below Schedule</li>
        <li class="is-no">Does NOT include Cancel for Any Reason (CFAR)***</li>
        <li class="is-no">No coverage for cancellations due to fear of a pandemic</li>
      </ul>
      <a class="plan-select" href="#">SELECT</a>
    </article>

    <article class="plan" style="top:555px;height:146px">
      <a class="plan-pdf" href="Note to Parents.pdf" target="_blank" aria-label="Open Note to Parents PDF"><svg width="13" height="13" viewBox="0 0 14 14"><rect x="2.5" y="1" width="9" height="12" rx="1" fill="none" stroke="#fff" stroke-width="1.2"/><text x="7" y="9" font-size="4.5" font-family="Roboto,sans-serif" font-weight="700" fill="#fff" text-anchor="middle">PDF</text></svg></a>
      <h3 class="plan-name">NONE</h3>
      <p class="plan-price"><sup>$</sup>0</p>
      <p class="plan-pitch">Potentially lose 100% of your tour cost</p>
      <ul class="plan-list"><li class="is-dot">No Payment Protection</li></ul>
      <a class="plan-select" href="#">SELECT</a>
    </article>
  </section>

  <table class="benefits m-table">
    <colgroup><col style="width:100px"><col style="width:27px"><col></colgroup>
    <tr><th class="b-head">Benefit</th><th>NONE</th><th>SCHOLAR<br>PRIME</th></tr>
    <tr style="height:28px"><td class="b-name">CANCEL FOR ANY REASON (CFAR)***</td><td class="x">✕</td><td class="x" style="padding-left:20px">✕</td></tr>
    <tr style="height:25px"><td class="b-name">Trip Cancellation**</td><td class="x">✕</td><td>Trip Cost*</td></tr>
    <tr style="height:24px"><td class="b-name">Trip Interruption**</td><td class="x">✕</td><td>150% Trip Cost</td></tr>
    <tr style="height:24px"><td class="b-name">Travel Delay – 6 Hours</td><td class="x">✕</td><td>$750 ($150/day)</td></tr>
    <tr style="height:32px"><td class="b-name">Missed Connection –<br>3 Hours</td><td class="x">✕</td><td>$500</td></tr>
    <tr style="height:26px"><td class="b-name">Baggage/Personal Effects</td><td class="x">✕</td><td>$1,500</td></tr>
    <tr style="height:22px"><td class="b-name">Baggage Delay – 24 Hours</td><td class="x">✕</td><td>$300</td></tr>
    <tr style="height:40px"><td class="b-name">Emergency Medical Evacuation, Medical Repatriation &amp; Return of Remains</td><td class="x">✕</td><td>$100,000</td></tr>
    <tr style="height:32px"><td class="b-name">Accident &amp; Sickness Medical Expense</td><td class="x">✕</td><td>$25,000</td></tr>
    <tr style="height:32px"><td class="b-name">Non-Medical Emergency Evacuation</td><td class="x">✕</td><td>$100,000</td></tr>
    <tr style="height:30px"><td class="b-name">Non-Insurance Worldwide Emergency Assistance Services</td><td class="x">✕</td><td>Included</td></tr>
  </table>
  <div class="abs m-scroll"></div>

  <div class="abs notes m-notes">
    <p>Coverages may vary and not all coverage is available in all jurisdictions. Totals listed below each coverage are the maximum benefit amount payable.</p>
    <p>* Up to the lesser of the Trip Cost paid or the limit of Coverage for which benefits are requested and the appropriate plan cost has been paid. Maximum limit of $10,000</p>
    <p>** For $0 Trip Cost, there is no Trip Cancellation and Trip Interruption is limited to $500 return air only</p>
    <p>*** CFAR coverage is the lessor of 75% of the nonrefundable trip cost or up to the maximum of $10,000. CFAR is optional and available for purchase on an individual level. Trip cancellation must be 48 hours or more prior to scheduled departure. CFAR must be purchased at the time of plan purchase and with, or before your final payment. CFAR is available if you paid your Travel Supplier for the full cost for all non-refundable trip costs for your trip prior to your cancellation of your trip. For $0 Trip Cost there is no CFAR. <b>This benefit is not available to residents of New York State.</b></p>
  </div>

  <a class="limits-btn m-limits" href="#">Click here for limitations and exclusions</a>

  <footer class="m-foot site-foot">
    © 2020 HALVARD TOURS, INC. RS, INC. &nbsp; CONTACT US &nbsp; (800) 555-0142 &nbsp; PRIVACY POLICY &nbsp; RESPONSIBILITY
    <span class="seal"></span>
  </footer>

</div>
</body>
</html>
```